Carver Lindqvist Group Business Cards

We have a new logo, and want to design new business cards with it. We are 21 years in business, and want a fresh but professional look, so not a lot of extra stuff on the card. We are a recruiting and staffing firm focused on placing accounting and finance professionals in the Dallas TX area. I've attached our new logo that should be displayed on the cards. Here is what I think we want on the cards:
Ray Pemberly, CPA
Partner and Managing Director
8282 Orchard Vale Rd.
Suite 610
Dallas, TX 75391
O 214-555-0184
M 214-555-0237
ray@carverlindqvist.example
www.carverlindqvist.example

```html
<!DOCTYPE html>
<html lang="en">
<head>
<meta charset="utf-8">
<title>Carver Lindqvist Group – Business Cards</title>
<link href="https://fonts.googleapis.com/css2?family=Montserrat:wght@400;500;600&display=swap" rel="stylesheet">
<style>
  :root {
    --brand-blue: #233e90;
    --ink: #333333;
    --rule: #a9a9a9;
    --paper: #ffffff;
    --backdrop: #d6d6d6;
  }
  * { margin: 0; padding: 0; box-sizing: border-box; }
  html, body {
    width: 1200px; height: 965px; overflow: hidden;
    background: var(--backdrop);
    font-family: "Montserrat", sans-serif;
  }
  .canvas { position: relative; width: 1200px; height: 965px; }
  .card {
    position: absolute; top: 159px;
    width: 383px; height: 669px;
  }
  .card-front { left: 186px; background: var(--paper); }
  .card-back { left: 653px; background: var(--brand-blue); }

  .brand {
    display: flex; align-items: center; gap: 10px;
    font-weight: 600; text-transform: uppercase; line-height: 1.15;
  }
  .brand-mark { width: 16px; height: 16px; flex: none; }
  .card-front .brand {
    position: absolute; left: 38px; top: 48px;
    color: var(--brand-blue); font-size: 20px;
  }
  .card-front .brand-mark { background: var(--brand-blue); }
  .card-back .brand {
    position: absolute; left: 0; right: 0; top: 300px;
    justify-content: center; color: var(--paper); font-size: 24px;
  }
  .card-back .brand-mark { background: var(--paper); width: 20px; height: 20px; }

  .person-name {
    position: absolute; left: 38px; top: 313px;
    font-size: 23px; font-weight: 500; color: var(--brand-blue);
    letter-spacing: 0.3px; white-space: nowrap;
  }
  .person-title {
    position: absolute; left: 38px; top: 342px;
    font-size: 16px; color: var(--ink);
  }
  .rule {
    position: absolute; left: 38px; width: 304px; height: 2px;
    background: var(--rule);
  }
  .contact-list {
    position: absolute; left: 38px; top: 406px; list-style: none;
    font-size: 16.5px; color: var(--ink);
  }
  .contact-list li { display: flex; align-items: center; height: 23px; white-space: nowrap; }
  .contact-icon { width: 13px; height: 13px; margin-right: 11px; flex: none; }
  .address {
    position: absolute; left: 38px; top: 526px;
    font-size: 17px; line-height: 22px; color: var(--ink); font-style: normal;
  }
  .website {
    position: absolute; left: 38px; top: 611px;
    font-size: 17px; color: var(--ink);
  }
  .website .domain { color: var(--brand-blue); }
</style>
</head>
<body>
<main class="canvas">
  <section class="card card-front">
    <div class="brand"><span class="brand-mark"></span><span>Carver Lindqvist<br>Group</span></div>

    <h1 class="person-name">RAY PEMBERLY, CPA</h1>
    <p class="person-title">Partner and Managing Director</p>

    <div class="rule" style="top:384px"></div>

    <ul class="contact-list">
      <li>
        <svg class="contact-icon" viewBox="0 0 16 16" aria-hidden="true"><path d="M3.5 1.5l2.5 0 1 3.5-1.8 1.2c.8 1.8 2 3 3.8 3.8L10.2 8.2l3.5 1v2.5c0 .8-.7 1.5-1.5 1.5C6.5 13 2 8.5 2 3c0-.8.7-1.5 1.5-1.5z" fill="none" stroke="var(--brand-blue)" stroke-width="1.6"/></svg>
        214-555-0184
      </li>
      <li>
        <svg class="contact-icon" viewBox="0 0 16 16" aria-hidden="true"><rect x="4" y="1.5" width="8" height="13" rx="1.2" fill="none" stroke="var(--brand-blue)" stroke-width="1.6"/><line x1="4" y1="11.5" x2="12" y2="11.5" stroke="var(--brand-blue)" stroke-width="1.4"/></svg>
        214-555-0237
      </li>
      <li>
        <svg class="contact-icon" viewBox="0 0 16 16" aria-hidden="true"><rect x="1.5" y="3.5" width="13" height="9" rx="1" fill="none" stroke="var(--brand-blue)" stroke-width="1.5"/><path d="M2 4.2l6 4.5 6-4.5" fill="none" stroke="var(--brand-blue)" stroke-width="1.5"/></svg>
        ray@carverlindqvist.example
      </li>
    </ul>

    <div class="rule" style="top:498px"></div>

    <address class="address">8282 Orchard Vale Rd. Suite<br>610 Dallas, TX 75391</address>

    <div class="rule" style="top:594px"></div>

    <p class="website">www.<span class="domain">carverlindqvist</span>.example</p>
  </section>

  <section class="card card-back">
    <div class="brand"><span class="brand-mark"></span><span>Carver Lindqvist Group</span></div>
  </section>
</main>
</body>
</html>
```